Business card design needed

We are a start up Mobile Vet Clinic.
We will be servicing an are that cover the Gladstone Region Shire.
Bookings will be made via the number listed or email address.
Travel will be charged

Target Market(s)

Pet Owners

Industry/Entity Type

Business

Contact Information for Business Card

BRINDELLA MOBILE VET
Tarrowen Pty Ltd
Dana Fosterby BVSc
27 Wexhaven St
Kestrelvale VIC 3984

PH: 0743186209 Fax: 0743186514 email: bmvet@quillnet.example

Logo styles of interest
Pictorial/Combination Logo

```html
<!DOCTYPE html>
<html lang="en">
<head>
<meta charset="utf-8">
<title>Brindella Mobile Vet – Business Card</title>
<link rel="stylesheet" href="https://fonts.googleapis.com/css2?family=Cabin:wght@400&display=swap">
<style>
  :root {
    --card-bg: #ffffff;
    --ink: #111111;
    --brand-blue: #2ba7e0;
    --paw-grey: #8a8a8a;
    --paw-dark: #3a3a3a;
  }
  * { box-sizing: border-box; margin: 0; padding: 0; }
  html, body {
    width: 1200px;
    height: 693px;
    overflow: hidden;
    background: var(--card-bg);
  }
  .card {
    position: relative;
    width: 1200px;
    height: 693px;
    overflow: hidden;
    background: var(--card-bg);
    font-family: "Cabin", sans-serif;
    color: var(--ink);
  }
  .business-name {
    position: absolute;
    top: 78px;
    left: 0;
    width: 1200px;
    text-align: center;
    font-size: 50px;
    line-height: 60px;
    font-weight: 400;
    letter-spacing: 0.3px;
    white-space: nowrap;
    color: var(--ink);
  }
  .vet-name {
    position: absolute;
    top: 240px;
    left: 0;
    width: 1200px;
    text-align: center;
    font-size: 46px;
    line-height: 56px;
    font-weight: 400;
    color: var(--brand-blue);
  }
  .contact-list {
    position: absolute;
    left: 55px;
    top: 424px;
    list-style: none;
    font-size: 37px;
    line-height: 51px;
    white-space: nowrap;
    color: var(--ink);
  }
  .paw-artwork {
    position: absolute;
    left: 779px;
    top: 291px;
    width: 384px;
    height: 341px;
    border-radius: 46% 46% 42% 42%;
    background: radial-gradient(circle at 50% 55%, var(--paw-grey) 0%, var(--paw-dark) 55%, var(--brand-blue) 78%);
  }
  .base-band {
    position: absolute;
    left: 0;
    bottom: 0;
    width: 1200px;
    height: 19px;
    background: var(--brand-blue);
  }
</style>
</head>
<body>
  <main class="card">
    <h1 class="business-name">BRINDELLA MOBILE VET Tarrowen Pty Ltd</h1>
    <p class="vet-name">Dana Fosterby</p>
    <ul class="contact-list">
      <li class="contact-address">BVSc 27 Wexhaven St Kestrelvale VIC 3984</li>
      <li class="contact-phone">PH: 0743186209</li>
      <li class="contact-fax">Fax: 0743186514</li>
      <li class="contact-email">email: bmvet@quillnet.example</li>
    </ul>
    <div class="paw-artwork" role="img" aria-label="Large blue-outlined paw print with a checkered fill"></div>
    <div class="base-band"></div>
  </main>
</body>
</html>
```